New Alcoholic Spiked Seltzer Line

We need a can design for a line of low calorie alcoholic seltzer. This product is a sparkling water and vodka drink with no sugar added in a slim 12 oz can.

This is a lighter, healthier, alternative to the sugary ready-to-drinks on the market. The product contains only 3 ingredients: Vodka, Water and Natural Flavors. It has only 100 calories but still has 5% alcohol, so you don't need to sacrifice alcohol to cut calories.

This product also does not contain any preservatives.

We want this design to communicate the following objectives to the consumer and in this order:

1. Appetizing product
2.Low calorie
3.Communicate the type of beverage (Spiked Seltzer)

The brand name of the product is VELKA.

The flavor of the product needed to be used for the design is Mango-Orange.

Comparable products are:

www.brisavelfizz.example/
https://www.tarnowbubble.example
https://quellrind.example/

The designs should not infringe or copy the creative directions of the products mentionned above. They are only given so that you can better understand the type of product we are developing.

Target Market(s)

Young Professional women between the ages of 25 and 44

Industry/Entity Type

Product

Colors

Designer to choose colors to be used in the design.

Requirements
Must have
• Design extendibility, meaning it can be adapted for other flavors.
• This is a new category in the market we are targeting, so consumers must easily be able to identify what type of product this is.

```html
<!DOCTYPE html>
<html lang="en">
<head>
<meta charset="utf-8">
<title>VELKA Spiked Seltzer – Can Label</title>
<link href="https://fonts.googleapis.com/css2?family=Oswald:wght@500;600&family=Russo+One&display=swap" rel="stylesheet">
<style>
  :root {
    --page-bg: #ffffff;
    --label-top: #f7d21c;
    --label-mid: #f6b51a;
    --label-bottom: #f08a12;
    --rim: #c9ccd0;
    --rim-dark: #9ea3a8;
    --ink-blue: #1f6fd6;
    --ink-green: #1e9b3a;
    --ink-dark: #3a2a0a;
    --ink-white: #ffffff;
    --brand-red: #e8401c;
    --slice-light: #ffd36a;
    --slice-deep: #f29a1c;
    --burst-core: #fff6c8;
    --burst-edge: rgba(255, 214, 90, 0);
  }
  * { box-sizing: border-box; margin: 0; padding: 0; }
  html, body {
    width: 1200px; height: 1200px; overflow: hidden;
    background: var(--page-bg);
  }
  .canvas { position: relative; width: 1200px; height: 1200px; }

  .can-label {
    position: absolute; left: 430px; top: 50px;
    width: 340px; height: 1100px;
    background: linear-gradient(180deg, var(--label-top) 0%, var(--label-mid) 45%, var(--label-bottom) 100%);
    border-radius: 6px;
    overflow: hidden;
    font-family: "Oswald", sans-serif;
    text-align: center;
  }
  .rim {
    position: absolute; left: 0; right: 0; height: 34px;
    background: linear-gradient(90deg, var(--rim-dark), var(--rim) 40%, #eef0f2 55%, var(--rim) 75%, var(--rim-dark));
  }
  .rim--top { top: 0; }
  .rim--bottom { bottom: 0; height: 20px; }

  .tagline {
    position: absolute; top: 62px; left: 0; right: 0;
    color: var(--ink-blue); font-size: 22px; font-weight: 600; letter-spacing: 0.5px;
  }
  .calorie-count {
    position: absolute; top: 120px; left: 50%; transform: translateX(-50%);
    width: 132px; height: 36px; background: var(--ink-green);
    color: var(--ink-white); font-size: 26px; font-weight: 600; line-height: 36px;
    letter-spacing: 18px; padding-left: 18px;
  }
  .calorie-word {
    position: absolute; top: 160px; left: 0; right: 0;
    color: var(--ink-green); font-size: 26px; font-weight: 600; letter-spacing: 3px;
  }
  .sugar-note {
    position: absolute; top: 205px; left: 0; right: 0;
    color: var(--ink-dark); font-size: 22px; font-weight: 500; letter-spacing: 1px;
  }

  .slice-art {
    position: absolute; top: 240px; left: 28px;
    width: 284px; height: 284px; border-radius: 50%;
    background: radial-gradient(circle, var(--slice-light) 0%, var(--slice-light) 55%, var(--slice-deep) 90%, #fff2c4 100%);
  }
  .brand-name {
    position: absolute; top: 296px; left: 0; right: 0;
    font-family: "Russo One", sans-serif; font-size: 88px; line-height: 1; font-weight: 400;
    color: var(--brand-red);
  }
  .product-kind {
    position: absolute; top: 388px; left: 0; right: 0;
    font-family: "Russo One", sans-serif; font-size: 28px; line-height: 1;
    color: var(--ink-blue); letter-spacing: 6px;
  }
  .product-type {
    position: absolute; top: 420px; left: 0; right: 0;
    font-family: "Russo One", sans-serif; font-size: 56px; line-height: 1;
    color: var(--ink-blue);
  }
  .flavour-note {
    position: absolute; top: 480px; left: 0; right: 0;
    color: var(--ink-dark); font-size: 17px; font-weight: 500; letter-spacing: 0.5px;
  }

  .burst {
    position: absolute; top: 560px; left: -60px; width: 460px; height: 340px;
    background: radial-gradient(ellipse at center, var(--burst-core) 0%, rgba(255,230,140,0.8) 25%, var(--burst-edge) 70%);
  }
  .fruit-art {
    position: absolute; top: 630px; left: 108px; width: 124px; height: 110px;
    border-radius: 50%;
    background: radial-gradient(circle at 40% 40%, #ffd84a 0%, #f7b418 60%, #e99a10 100%);
  }

  .flavour-name {
    position: absolute; top: 900px; left: 0; right: 0;
    color: var(--ink-white); font-size: 26px; font-weight: 600; letter-spacing: 3px;
  }
  .flavour-rule {
    position: absolute; top: 942px; left: 60px; width: 220px; height: 2px;
    background: var(--ink-white);
  }
  .calorie-claim {
    position: absolute; top: 952px; left: 0; right: 0;
    color: var(--ink-white); font-size: 26px; font-weight: 600; letter-spacing: 3px;
  }
  .volume {
    position: absolute; top: 1004px; left: 0; right: 0;
    color: var(--ink-white); font-size: 18px; font-weight: 500; letter-spacing: 1px;
  }
</style>
</head>
<body>
<main class="canvas">
  <section class="can-label">
    <div class="rim rim--top"></div>

    <p class="tagline">LIGHTER AND HEALTHIER</p>
    <p class="calorie-count">100</p>
    <p class="calorie-word">CALORIES</p>
    <p class="sugar-note">NO SUGAR ADDED</p>

    <div class="slice-art" role="img" aria-label="Orange slice illustration behind the brand name"></div>
    <h1 class="brand-name">VELKA</h1>
    <p class="product-kind">SPIKED</p>
    <p class="product-type">SELTZER</p>
    <p class="flavour-note">VODKA &amp; NATURAL FLAVOUR</p>

    <div class="burst" role="img" aria-label="Radiating sunburst and halftone dots"></div>
    <div class="fruit-art" role="img" aria-label="Illustration of a mango and orange with leaf and a cut slice"></div>

    <p class="flavour-name">MANGO-ORANGE</p>
    <div class="flavour-rule"></div>
    <p class="calorie-claim">LOW CALORIE</p>
    <p class="volume">12 FL OZ (355ML) · 5% ALC/VOL</p>

    <div class="rim rim--bottom"></div>
  </section>
</main>
</body>
</html>
```